Junior Rugby Event needs 4 page Brochure

4 Page A4 brochure to be designed for a junior rugby event to be held in japan.. The brochure will entice coaches, teachers and players to the event.
The brochure will provide a basic overview of the event - dates, venue and promote some of the key features of the host, venue and event.
Event logo has been included. Design overview with copy has been included as word document. Images have been attached that can be used or alternatives sourced. A PDF document has been included of a design example that we like.
Rugby Clubs and Schools
Events

```html
<!DOCTYPE html>
<html lang="en">
<head>
<meta charset="utf-8">
<title>Pacific Junior Rugby Invitational – Brochure</title>
<link href="https://fonts.googleapis.com/css2?family=Open+Sans:ital,wght@0,400;0,600;0,700;0,800;1,400&display=swap" rel="stylesheet">
<style>
:root{
  --red:#d4253a;
  --red-deep:#a9172b;
  --navy:#1f2a5a;
  --navy-deep:#151d44;
  --slate:#4a4f6e;
  --white:#ffffff;
  --paper:#f3f4f7;
  --stage:#e6e8ee;
  --ink:#1c2340;
}
*{box-sizing:border-box;margin:0;padding:0}
html,body{width:841px;height:1200px;overflow:hidden}
body{background:var(--stage);font-family:"Open Sans",Arial,sans-serif;color:var(--white);position:relative}
.spread{position:absolute;left:20px;width:800px;height:566px;display:flex;box-shadow:0 6px 18px rgba(20,25,50,.25)}
.spread--outer{top:24px}
.spread--inner{top:610px}
.page{position:relative;width:400px;height:566px;overflow:hidden}
.abs{position:absolute}
.photo{position:absolute}

/* Back page */
.back{background:linear-gradient(160deg,var(--red) 0%,var(--red-deep) 100%)}
.back__title{left:30px;top:40px;width:340px;font-weight:800;font-size:18px;text-align:center;letter-spacing:.3px}
.back__intro{left:30px;top:70px;width:340px;font-size:8.5px;line-height:1.45;text-align:center}
.package-bar{left:0;width:260px;height:20px;background:var(--navy);font-weight:700;font-size:10px;line-height:20px;padding-left:30px}
.package-list{left:38px;width:220px;font-size:8.5px;line-height:1.55;list-style:disc}
.package-photo{width:104px;height:104px;border-radius:50%;border:4px solid var(--white)}
.back__contact{left:30px;top:392px;width:340px;font-size:8.5px;line-height:1.5;text-align:center}
.back__contact strong{display:block;font-size:10px;font-weight:700;margin-top:4px}
.strip-white{left:0;width:400px;height:34px;background:var(--white);color:var(--navy);font-weight:800;font-size:13px;line-height:34px;padding-left:30px}
.strip-red{left:0;width:400px;background:var(--red);font-weight:800;font-size:14px;text-align:right;padding-right:30px}

/* Front page */
.front{background:var(--navy)}
.event-mark{right:18px;top:20px;display:flex;align-items:center;gap:6px;background:var(--white);padding:6px 10px;border-radius:4px;color:var(--navy);font-weight:800;font-size:10px;line-height:1.15;width:120px}
.event-mark__dot{width:14px;height:14px;border-radius:50%;background:var(--red);flex:none}
.title-band{left:0;width:400px;display:block}
.title-band--navy{background:var(--navy)}
.title-band--red{background:var(--red)}
.title-year{top:330px;height:52px;font-weight:800;font-size:38px;line-height:52px;text-align:center;letter-spacing:.5px}
.title-name{top:382px;height:38px;font-weight:800;font-size:20px;line-height:38px;text-align:center}
.title-dates{top:420px;height:36px;font-size:17px;line-height:36px;text-align:center;font-weight:600}
.title-dates b{font-weight:800}
.title-place{top:456px;height:36px;font-weight:800;font-size:15px;line-height:36px;text-align:center}
.title-web{top:492px;height:40px;background:var(--white);color:var(--navy);font-weight:800;font-size:14px;line-height:40px;text-align:center}
.title-foot{top:532px;height:34px;background:var(--navy-deep)}

/* Inner left */
.overview{background:var(--paper)}
.overview__panel{left:0;top:180px;width:400px;height:222px;background:var(--red)}
.overview__heading{left:0;top:194px;width:400px;text-align:center;font-weight:800;font-size:18px}
.overview__text{left:30px;top:224px;width:340px;font-size:8.5px;line-height:1.5;text-align:center}
.overview__invite{left:30px;top:372px;width:340px;font-weight:800;font-size:9px;text-align:center}
.sign-band{left:0;top:402px;width:400px;height:46px;background:var(--white)}
.sign-name{left:30px;top:414px;font-style:italic;font-size:15px;color:var(--ink)}
.sign-role{left:170px;top:406px;font-weight:800;font-size:13px;color:var(--red)}
.sign-role small{display:block;font-size:9px;color:var(--navy);font-weight:700}
.venue{left:0;top:448px;width:400px;height:118px;background:var(--navy)}
.venue__heading{left:0;top:456px;width:400px;text-align:center;font-weight:800;font-size:16px}
.venue__text{left:30px;top:482px;width:340px;font-size:8.5px;line-height:1.5;text-align:center}

/* Inner right */
.destination{background:linear-gradient(180deg,var(--slate) 0%,var(--navy) 60%)}
.where__heading{left:0;top:52px;width:400px;text-align:center;font-weight:800;font-size:18px}
.where__text{left:30px;top:80px;width:340px;font-size:8.5px;line-height:1.5;text-align:center}
.where__text p+p{margin-top:6px}
.who{left:20px;top:238px;width:360px;height:100px;background:var(--red);border-radius:10px}
.who__heading{left:0;top:246px;width:400px;text-align:center;font-weight:800;font-size:16px}
.who__text{left:40px;top:272px;width:320px;font-size:8.5px;line-height:1.5;text-align:center}
.who__text b{font-weight:800;font-size:10px}
</style>
</head>
<body>

<section class="spread spread--outer">
  <article class="page back">
    <h2 class="abs back__title">TRAVEL &amp; TOURNAMENT PACKAGE</h2>
    <p class="abs back__intro">Our aim is to make participation easy. Packages below cover travel, stay and match days so your squad can focus on rugby while discovering the culture of a great host city.</p>

    <div class="abs package-bar" style="top:122px">Harbour Sports Park Player Package</div>
    <ul class="abs package-list" style="top:148px">
      <li>Five nights accommodation with breakfast</li>
      <li>Airport transfers and daily team bus</li>
      <li>Guaranteed tournament matches</li>
      <li>Training sessions with local coaches</li>
      <li>Welcome dinner and closing ceremony</li>
      <li>Official team kit and event pack</li>
    </ul>
    <div class="photo package-photo" style="left:266px;top:134px;background:linear-gradient(160deg,#4d7a5e,#2b4a3a)" role="img" aria-label="Sports park entrance sign on artificial turf"></div>

    <div class="abs package-bar" style="top:262px">Fukuoka Player or Supporter Package</div>
    <ul class="abs package-list" style="top:288px">
      <li>Five nights accommodation in city centre</li>
      <li>Guided tours of shrines and markets</li>
      <li>Tickets to a professional match</li>
      <li>Supporter seating at all finals</li>
      <li>Local transport pass included</li>
    </ul>
    <div class="photo package-photo" style="left:266px;top:274px;background:linear-gradient(160deg,#8a3a4a,#3a2a4a)" role="img" aria-label="Colourful Fukuoka street signs at night"></div>

    <div class="abs back__contact">Please contact us to receive a tailored quote for your team for the Pacific Junior Rugby Invitational.
      <strong>hello@pacificjuniorrugby.example</strong>
    </div>

    <div class="abs strip-white" style="top:470px">pacificjuniorrugby.example</div>
    <div class="abs strip-red" style="top:504px;height:62px;line-height:62px">FUKUOKA, JAPAN</div>
  </article>

  <article class="page front">
    <svg class="abs" style="left:0;top:0" width="400" height="330" viewBox="0 0 400 330">
      <defs>
        <linearGradient id="lineout-tone" x1="0" y1="0" x2="0" y2="1">
          <stop offset="0" stop-color="#3a4a7c"/>
          <stop offset="1" stop-color="#26315f"/>
        </linearGradient>
        <linearGradient id="turf-tone" x1="0" y1="0" x2="0" y2="1">
          <stop offset="0" stop-color="#4f6a5a"/>
          <stop offset="1" stop-color="#3d6a48"/>
        </linearGradient>
      </defs>
      <path d="M0 0H230C170 80 170 240 230 330H0Z" fill="url(#lineout-tone)" role="img" aria-label="Junior players jumping for the ball in a lineout"/>
      <path d="M230 0H400V330H230C170 240 170 80 230 0Z" fill="url(#turf-tone)" role="img" aria-label="Rugby ball resting on grass with players training behind"/>
      <path d="M230 0C170 80 170 240 230 330" fill="none" stroke="#ffffff" stroke-width="5"/>
    </svg>
    <div class="abs event-mark"><span class="event-mark__dot"></span><span>PACIFIC JUNIOR RUGBY</span></div>

    <h1>
      <span class="abs title-band title-band--navy title-year">2019 PACIFIC</span>
      <span class="abs title-band title-band--red title-name">JUNIOR RUGBY INVITATIONAL</span>
    </h1>
    <p class="abs title-band title-band--navy title-dates">30TH SEPTEMBER TO <b>4TH OCTOBER 2019</b></p>
    <p class="abs title-band title-band--red title-place">FUKUOKA, JAPAN</p>
    <p class="abs title-band title-web">pacificjuniorrugby.example</p>
    <div class="abs title-band title-foot"></div>
  </article>
</section>

<section class="spread spread--inner">
  <article class="page overview">
    <svg class="abs" style="left:0;top:0" width="400" height="200" viewBox="0 0 400 200">
      <defs>
        <linearGradient id="huddle-tone" x1="0" y1="0" x2="0" y2="1">
          <stop offset="0" stop-color="#7e97b0"/>
          <stop offset="1" stop-color="#4f6f8e"/>
        </linearGradient>
      </defs>
      <path d="M40 200C20 120 60 20 200 10C340 0 390 90 380 200Z" fill="url(#huddle-tone)" role="img" aria-label="Junior team in a huddle on the pitch"/>
      <path d="M40 200C20 120 60 20 200 10C340 0 390 90 380 200" fill="none" stroke="#ffffff" stroke-width="5"/>
    </svg>
    <div class="abs overview__panel"></div>
    <h2 class="abs overview__heading">TOURNAMENT OVERVIEW</h2>
    <p class="abs overview__text">The Pacific Junior Rugby Invitational brings school and club teams together for a week of competitive rugby in the host city of a major international tournament. Teams from Japan, Asia, Oceania, Europe and the Americas will play in age grade pools, with every squad guaranteed matches against new opponents. Beyond the pitch, players will share cultural visits, coaching clinics and a festival day, building friendships that last well after the final whistle.</p>
    <p class="abs overview__invite">WE INVITE YOU TO JOIN US IN JAPAN FOR THIS CELEBRATION OF RUGBY.</p>
    <div class="abs sign-band"></div>
    <p class="abs sign-name">Daniel Harper</p>
    <p class="abs sign-role">CHAIRMAN<small>PACIFIC JUNIOR RUGBY INVITATIONAL</small></p>
    <div class="abs venue"></div>
    <h2 class="abs venue__heading">VENUE</h2>
    <p class="abs venue__text">Harbour Sports Park is a modern multi sport venue with several full size rugby fields, grandstand seating, changing rooms and medical facilities. In addition to the fields, the park offers a gym, recovery pools and team meeting rooms, with hotels and restaurants a short walk away.</p>
  </article>

  <article class="page destination">
    <h2 class="abs where__heading">WHERE</h2>
    <div class="abs where__text">
      <p>Fukuoka is the largest city on the island of Kyushu and a regional hub with direct flights to Tokyo, Osaka, Shanghai, Seoul, Bangkok, Taipei and Singapore.</p>
      <p>Fukuoka is host to one of the 2019 world cup venues, a stadium with a capacity of over twenty thousand, and the city will welcome fans from around the globe during the event.</p>
      <p>Teams will have the chance to watch international pool matches during their stay, including fixtures on the opening weekend of October.</p>
    </div>
    <div class="abs who"></div>
    <h2 class="abs who__heading">WHO</h2>
    <p class="abs who__text">The tournament will feature <b>U17, U15 &amp; U13</b> categories and is open to club, school and development teams. Each age category will be seeded with the ability to play off for Plate, Bowl and Trophy divisions.</p>
    <svg class="abs" style="left:0;top:330px" width="400" height="236" viewBox="0 0 400 236">
      <defs>
        <linearGradient id="shrine-tone" x1="0" y1="0" x2="0" y2="1">
          <stop offset="0" stop-color="#a9b4c4"/>
          <stop offset="0.45" stop-color="#b5483e"/>
          <stop offset="1" stop-color="#8a8d96"/>
        </linearGradient>
      </defs>
      <path d="M0 40C120 10 280 0 400 30V236H0Z" fill="url(#shrine-tone)" role="img" aria-label="Red shrine gate and steps under a pale sky"/>
      <path d="M0 40C120 10 280 0 400 30" fill="none" stroke="#ffffff" stroke-width="5"/>
    </svg>
  </article>
</section>

</body>
</html>
```